Corvane Supplies Business Card

Professional business card that stand out to our potential customers. Front and back with clean modern design

Industry/Entity Type

Oil and gas

Contact Information for Business Card

Name, address, website , office phone and cell number

Requirements
Must have
• Editable files for each employee

```html
<!DOCTYPE html>
<html lang="en">
<head>
<meta charset="utf-8">
<title>Corvane Supplies Business Card</title>
<link href="https://fonts.googleapis.com/css2?family=Michroma&family=Roboto:wght@400;500;700&family=Lato:wght@400&display=swap" rel="stylesheet">
<style>
  :root {
    --brand-red: #e8262d;
    --brand-blue: #12b0d4;
    --card-black: #0b0b0b;
    --card-paper: #ececec;
    --ink: #1f1f1f;
    --backdrop: #dcdcdc;
    --white: #ffffff;
  }
  * { box-sizing: border-box; margin: 0; padding: 0; }
  html, body {
    width: 1200px; height: 1000px; overflow: hidden;
    background: var(--backdrop);
  }
  .canvas { position: relative; width: 1200px; height: 1000px; }

  .card {
    position: absolute; width: 600px; height: 343px;
    box-shadow: 0 10px 24px rgba(0,0,0,0.18);
    overflow: hidden;
  }

  /* Back of card */
  .card-back {
    left: 80px; top: 90px;
    background: var(--card-black);
    display: flex; flex-direction: column; align-items: center; justify-content: center;
  }
  .card-back .brand-name {
    font-family: "Roboto", sans-serif; font-weight: 700;
    font-size: 34px; letter-spacing: 2px; color: var(--brand-red);
    display: flex; align-items: center; gap: 14px;
  }
  .brand-mark { width: 22px; height: 22px; background: var(--brand-blue); }
  .card-back .website {
    margin-top: 34px;
    font-family: "Lato", sans-serif; font-size: 17px; letter-spacing: 3px;
    color: var(--white);
  }

  /* Front of card */
  .card-front {
    left: 520px; top: 520px;
    background: var(--card-paper);
  }
  .card-front .logo-zone {
    position: absolute; left: 0; top: 0; width: 270px; height: 300px;
    display: flex; align-items: center; justify-content: center;
  }
  .card-front .brand-name {
    font-family: "Roboto", sans-serif; font-weight: 700;
    font-size: 24px; letter-spacing: 1px; color: var(--brand-red);
    display: flex; align-items: center; gap: 10px;
  }
  .card-front .brand-mark { width: 16px; height: 16px; }
  .divider {
    position: absolute; left: 272px; top: 38px; width: 1px; height: 222px;
    background: var(--brand-blue);
  }
  .identity { position: absolute; left: 300px; top: 44px; }
  .person-name {
    font-family: "Michroma", sans-serif; font-weight: 400;
    font-size: 21px; color: var(--brand-red); letter-spacing: 0.5px;
    -webkit-text-stroke: 0.6px var(--brand-red);
  }
  .person-role {
    margin-top: 2px;
    font-family: "Roboto", sans-serif; font-size: 15px; font-weight: 500;
    color: var(--ink); letter-spacing: 1px;
  }
  .contact-list {
    position: absolute; left: 318px; top: 140px; list-style: none;
    font-family: "Roboto", sans-serif; font-size: 15px; color: var(--ink);
  }
  .contact-list li { display: flex; align-items: flex-start; gap: 9px; line-height: 22px; }
  .contact-list svg { width: 15px; height: 15px; margin-top: 3px; flex: none; fill: var(--brand-blue); }
  .color-band { position: absolute; left: 0; bottom: 0; width: 600px; height: 14px; }
</style>
</head>
<body>
<main class="canvas">

  <section class="card card-back" aria-label="Card back">
    <div class="brand-name"><span class="brand-mark"></span>CORVANE SUPPLIES</div>
    <div class="website">WWW.CORVANESUPPLIES.COM</div>
  </section>

  <section class="card card-front" aria-label="Card front">
    <div class="logo-zone">
      <div class="brand-name"><span class="brand-mark"></span>CORVANE SUPPLIES</div>
    </div>
    <div class="divider"></div>
    <div class="identity">
      <h1 class="person-name">MARCUS HALE</h1>
      <p class="person-role">MANAGING DIRECTOR</p>
    </div>
    <ul class="contact-list">
      <li>
        <svg viewBox="0 0 16 16" aria-hidden="true"><rect x="1" y="4" width="14" height="11" rx="1"/><rect x="3" y="1" width="10" height="4" rx="1"/></svg>
        <span>044-555 210 347</span>
      </li>
      <li>
        <svg viewBox="0 0 16 16" aria-hidden="true"><rect x="5" y="1" width="7" height="14" rx="1.5"/><rect x="1" y="5" width="1.5" height="6"/><rect x="14" y="5" width="1.5" height="6"/></svg>
        <span>011-555 876 902</span>
      </li>
      <li>
        <svg viewBox="0 0 16 16" aria-hidden="true"><path d="M15 1 1 7l5 2 2 6z"/></svg>
        <span>info@corvanesupplies.com</span>
      </li>
      <li>
        <svg viewBox="0 0 16 16" aria-hidden="true"><path d="M8 1a5 5 0 0 0-5 5c0 4 5 9 5 9s5-5 5-9a5 5 0 0 0-5-5zm0 7a2 2 0 1 1 0-4 2 2 0 0 1 0 4z"/></svg>
        <span>4570 Harbor Ridge Pkwy,<br>212-B, FL 32541</span>
      </li>
    </ul>
    <svg class="color-band" viewBox="0 0 600 14" preserveAspectRatio="none" aria-hidden="true">
      <polygon points="0,0 300,0 294,14 0,14" fill="var(--brand-red)"/>
      <polygon points="304,0 600,0 600,14 298,14" fill="var(--brand-blue)"/>
    </svg>
  </section>

</main>
</body>
</html>
```